Ringordner
Zielgruppe
Wir sind ein ambulanter Pflegedienst, der im Raum Dessau-Roßlau tätig ist. Wir haben uns mit einer Tagespflege erweitert. Zukünftig ist es geplant, dass wir uns um eine Therapie erweitern. Unsere Zielgruppe sind sämtliche Pflegebedürftige und deren Angehörige. Für die aktuelle Maßnahme sind jedoch die zukünftigen Mitarbeiter im Vordergrund.
Aufgabenstellung
Ich möchte für unsere zukünftigen Mitarbeiter einen A4 Ringordner mit zwei Klammern gestalten. Dieser Ordner wird als Willkomm Mappe für neue Mitarbeiter bei der Aufnahme der Tätigkeit übergeben. Das Design sollte das Hauptlogo des Pflegedienstes enthalten und auf die Tochterfirmen hinweisen. Es sollte modern und frisch wirken und vor allem professionell. Es soll die Mitarbeiter in unserer neuen Firma willkommen heißen.
Dann benötige ich ein zweites Design, dass für die Kunden ist. Es beinhaltet einen Leitfaden, was für die Zusammenarbeit zwischen Pflegedienst und Patient am wichtigsten ist. Dieses Design ist genauso wie beim Mitarbeiter ein A4 Ringordner mit zwei Klammern. Auch dieser Ordner soll diesmal den Patienten bekommen heißen. Hier soll auch das Logo des Pflegedienstes enthalten sein und auch die Tochterfirmen hinweisen.

```html
<!DOCTYPE html>
<html lang="de">
<head>
<meta charset="utf-8">
<title>Ringordner – Pflegeteam Auengrund</title>
<link href="https://fonts.googleapis.com/css2?family=Montserrat:wght@400;500;600;700&family=Playfair+Display&display=swap" rel="stylesheet">
<style>
  :root {
    --bg: #e4e4e6;
    --cover: #f7f7f7;
    --teal: #2fb0ae;
    --teal-dark: #1f7d7a;
    --green: #7bbd45;
    --ink: #3c3c3c;
    --muted: #8a8a8a;
    --orange: #e7a45a;
    --photo-a: #d9d2c6;
    --photo-b: #9a8a76;
  }
  * { margin: 0; padding: 0; box-sizing: border-box; }
  html, body { width: 1200px; height: 1009px; overflow: hidden; background: var(--bg); }
  body { position: relative; font-family: "Montserrat", sans-serif; color: var(--ink); }

  .binder-cover {
    position: absolute; left: 275px; top: 45px; width: 650px; height: 920px;
    background: var(--cover);
    box-shadow: 0 10px 30px rgba(0,0,0,.12);
    overflow: hidden;
  }

  .brand {
    position: absolute; top: 70px; left: 0; right: 0;
    display: flex; align-items: center; justify-content: center; gap: 14px;
  }
  .brand-dot { width: 30px; height: 30px; border-radius: 50%; background: var(--teal); }
  .brand-name { font-weight: 600; font-size: 22px; letter-spacing: 1px; color: var(--ink); text-transform: uppercase; }

  .care-photo { position: absolute; left: 400px; top: 210px; width: 250px; height: 400px; }

  .intro { position: absolute; left: 60px; top: 250px; width: 330px; }
  .intro-kicker { font-family: "Playfair Display", serif; font-size: 15px; color: var(--muted); margin-bottom: 6px; }
  .intro-title { font-weight: 700; font-size: 26px; line-height: 1.1; color: var(--teal); margin-bottom: 12px; }
  .intro-text { font-size: 11.5px; line-height: 1.35; color: var(--muted); }

  .services { position: absolute; left: 60px; top: 480px; width: 430px; }
  .services-title { font-weight: 600; font-size: 25px; margin-bottom: 10px; }
  .services-title .accent-a { color: var(--teal-dark); }
  .services-title .accent-b { color: var(--green); }
  .services-list { list-style: none; font-size: 14px; line-height: 1.55; color: var(--ink); font-weight: 500; }
  .services-list li::before { content: "• "; }

  .partner {
    position: absolute; left: 60px; top: 790px;
    display: flex; align-items: center; gap: 10px;
  }
  .partner-square { width: 26px; height: 26px; background: var(--orange); }
  .partner-name { font-weight: 500; font-size: 17px; color: var(--orange); }
</style>
</head>
<body>
  <main class="binder-cover">
    <header class="brand">
      <span class="brand-dot"></span>
      <span class="brand-name">Pflegeteam Auengrund</span>
    </header>

    <svg class="care-photo" viewBox="0 0 250 400">
      <defs>
        <linearGradient id="photoTone" x1="0" y1="0" x2="1" y2="1">
          <stop offset="0" stop-color="var(--photo-a)"/>
          <stop offset="1" stop-color="var(--photo-b)"/>
        </linearGradient>
      </defs>
      <path d="M30 20 C70 -5 150 10 250 95 L250 330 C200 400 150 410 110 360 C70 310 45 230 22 150 C5 90 10 40 30 20 Z"
            fill="url(#photoTone)" role="img" aria-label="Foto: ältere Dame und junge Pflegerin halten sich lächelnd an den Händen"/>
      <path d="M14 100 C14 30 60 0 120 15 C170 30 215 70 250 100" fill="none" stroke="var(--teal)" stroke-width="6" stroke-linecap="round"/>
      <path d="M2 200 C40 185 80 200 105 270" fill="none" stroke="var(--green)" stroke-width="4" stroke-linecap="round"/>
      <path d="M4 178 C50 172 90 200 112 285" fill="none" stroke="var(--teal)" stroke-width="4" stroke-linecap="round"/>
    </svg>

    <section class="intro">
      <p class="intro-kicker">Der Mensch im Mittelpunkt</p>
      <h1 class="intro-title">Für uns ist Pflege eine Herzensangelegenheit</h1>
      <p class="intro-text">Für unseren ambulanten Pflegedienst steht die Pflege von Mensch zu Mensch im Mittelpunkt. Es ist unser Ziel, die Fähigkeiten und Möglichkeiten der Menschen zu erhalten und zu fördern, damit sie ihr Leben so lange wie möglich unabhängig führen und gestalten können.</p>
    </section>

    <section class="services">
      <h2 class="services-title"><span class="accent-a">Unsere</span> <span class="accent-b">Leistungen</span></h2>
      <ul class="services-list">
        <li>Grundpflege</li>
        <li>Behandlungspflege</li>
        <li>Beratungseinsatz nach §37 Abs. 3 SGB XI</li>
        <li>Verhinderungspflege nach §39 SGB XI</li>
        <li>Entlastungs- und Betreuungsangebote gem. §45b SGB XI</li>
        <li>Hauswirtschaftliche Leistungen</li>
        <li>Sonstige Leistungen</li>
      </ul>
    </section>

    <footer class="partner">
      <span class="partner-square"></span>
      <span class="partner-name">Tagespflege Haus Marlene</span>
    </footer>
  </main>
</body>
</html>
```